Folded A4 flyer for design&construction company

Folded A4 flyer needed. Keywords: elegant, stylish
our website www.corvimo.ae

Industry/Entity Type

Construction

```html
<!DOCTYPE html>
<html lang="en">
<head>
<meta charset="utf-8">
<title>Corvimo – Folded A4 Flyer</title>
<link href="https://fonts.googleapis.com/css2?family=Lato:wght@400;700&family=Montserrat:wght@500;600;700&display=swap" rel="stylesheet">
<style>
  :root{
    --gold:#f2b300;
    --gold-deep:#e09a00;
    --ink:#2b2b2b;
    --paper:#f4f4f4;
    --paper-shade:#e6e6e6;
    --stage:#e4e4e4;
  }
  html,body{margin:0;padding:0;overflow:hidden;}
  body{width:1200px;height:1200px;background:var(--stage);position:relative;}
  .spread{position:absolute;left:40px;top:204px;width:1120px;height:792px;display:flex;box-shadow:0 10px 30px rgba(0,0,0,.18);}
  .page{position:relative;width:560px;height:792px;overflow:hidden;background:var(--paper);}
  .page svg.art{position:absolute;inset:0;width:560px;height:792px;}
  .brand{position:absolute;font-family:"Montserrat",sans-serif;font-weight:500;color:var(--ink);letter-spacing:1px;text-align:center;}
  .cover .brand{left:70px;top:100px;width:260px;font-size:44px;}
  .back .brand{left:0;top:176px;width:560px;font-size:46px;}
  .quote{position:absolute;left:0;width:560px;text-align:center;font-family:"Montserrat",sans-serif;font-weight:600;font-size:31px;line-height:1.15;}
  .quote .line-dark{color:var(--ink);}
  .quote .line-gold{color:var(--gold);}
  .intro{position:absolute;left:58px;top:42px;width:444px;margin:0;font-family:"Lato",sans-serif;font-size:12.6px;line-height:1.3;color:var(--ink);text-align:justify;text-align-last:center;}
  .cta{position:absolute;left:0;width:560px;text-align:center;font-family:"Montserrat",sans-serif;}
  .cta-title{top:560px;font-weight:700;font-size:31px;color:#fff;}
  .cta-contact{top:608px;font-weight:500;font-size:20px;color:var(--ink);}
</style>
</head>
<body>
<div class="spread">

  <section class="page cover">
    <svg class="art" viewBox="0 0 560 792" xmlns="http://www.w3.org/2000/svg">
      <defs>
        <linearGradient id="interiorTone" x1="0" y1="0" x2="1" y2="1">
          <stop offset="0" stop-color="#fbe9cf"/>
          <stop offset=".45" stop-color="#f1b24a"/>
          <stop offset="1" stop-color="#b97a2e"/>
        </linearGradient>
        <linearGradient id="goldBand" x1="0" y1="0" x2="1" y2="0">
          <stop offset="0" stop-color="var(--gold-deep)"/>
          <stop offset="1" stop-color="var(--gold)"/>
        </linearGradient>
      </defs>
      <rect width="560" height="792" fill="var(--paper)"/>
      <rect width="560" height="330" fill="url(#goldBand)"/>
      <path d="M0,600 C180,560 330,480 560,520 L560,560 C340,520 190,600 0,650 Z" fill="var(--gold)"/>
      <path class="photo" role="img" aria-label="Photo of a bright modern interior with curved orange walls, wooden floor and lounge chairs"
            d="M0,240 C170,220 320,130 560,50 L560,520 C400,470 230,560 0,610 Z" fill="url(#interiorTone)"/>
      <path d="M0,610 C230,560 400,470 560,520" fill="none" stroke="var(--ink)" stroke-width="6"/>
      <ellipse cx="200" cy="125" rx="135" ry="100" fill="#fff" stroke="var(--ink)" stroke-width="7"/>
      <path d="M0,752 C200,730 380,745 560,720 L560,792 L0,792 Z" fill="url(#goldBand)"/>
    </svg>
    <div class="brand">CORVIMO</div>
    <div class="quote" style="top:650px;">
      <div class="line-dark">QUALITY IS NOT AN ACT</div>
      <div class="line-gold">IT IS A HABIT – ANONYMOUS</div>
    </div>
  </section>

  <section class="page back">
    <svg class="art" viewBox="0 0 560 792" xmlns="http://www.w3.org/2000/svg">
      <defs>
        <linearGradient id="loungeTone" x1="0" y1="0" x2="1" y2="1">
          <stop offset="0" stop-color="#6b4a2c"/>
          <stop offset=".6" stop-color="#c79a5c"/>
          <stop offset="1" stop-color="#e3c08a"/>
        </linearGradient>
        <linearGradient id="roomTone" x1="0" y1="0" x2="1" y2="1">
          <stop offset="0" stop-color="#f6e6c6"/>
          <stop offset=".6" stop-color="#d9a764"/>
          <stop offset="1" stop-color="#a8743c"/>
        </linearGradient>
        <linearGradient id="goldFill" x1="0" y1="0" x2="0" y2="1">
          <stop offset="0" stop-color="var(--gold)"/>
          <stop offset="1" stop-color="var(--gold-deep)"/>
        </linearGradient>
      </defs>
      <rect width="560" height="792" fill="var(--paper)"/>
      <path d="M0,480 C170,430 360,470 560,390 L560,745 L0,745 Z" fill="url(#goldFill)"/>
      <path d="M0,480 C170,430 360,470 560,390" fill="none" stroke="var(--ink)" stroke-width="6"/>
      <rect y="745" width="560" height="47" fill="var(--ink)"/>
      <circle cx="165" cy="375" r="104" fill="#fff" stroke="var(--ink)" stroke-width="8"/>
      <circle role="img" aria-label="Photo of a lounge with a modern chair on a wooden deck floor" cx="165" cy="375" r="92" fill="url(#loungeTone)"/>
      <circle cx="378" cy="352" r="112" fill="#fff" stroke="var(--ink)" stroke-width="8"/>
      <circle role="img" aria-label="Photo of a warm-lit bathroom interior with an open door" cx="378" cy="352" r="100" fill="url(#roomTone)"/>
    </svg>
    <p class="intro">We believe in quality beginnings and flawless finishes. We are a team of creative designers and constructors with years of experience and expertise in providing complete interior design and construction services. Our unique designing prowess is complemented by our unflinching commitment to quality construction. Our team specializes in classic and contemporary high quality construction in Dubai for commercial and residential projects.</p>
    <div class="brand">CORVIMO</div>
    <div class="cta cta-title">GET A FREE QUOTE TODAY!</div>
    <div class="cta cta-contact">800 – CORVIMO OR CONTACT@CORVIMO.AE</div>
  </section>

</div>
</body>
</html>
```